MD Business Card

I want to create a simple business card.
I am a consultant. I design and develop furniture, lighting and accessories for hospitality and retail brands.
I want the card to be simple and clean. Not too much of a logo - but it needs the basic information shown on the attached file.
Also - I have shown some fonts that I like on the attached file.
The card can be square or rectangle. It should be double sided.
I prefer 1-2 colors (not too colorful - but using color an an accent) Even if using color on the edges as an accent.

My snapquilt link shows some other graphics styles that I like. I like clean and simple.
http://www.snapquilt.com/marendowsett/business-cards/

Reason: I needed a few more days to see some of the options evolve.

Hospitality

```html
<!DOCTYPE html>
<html lang="en">
<head>
<meta charset="utf-8">
<title>MD Business Card</title>
<link href="https://fonts.googleapis.com/css2?family=Oswald:wght@300;400;700&display=swap" rel="stylesheet">
<style>
  :root {
    --paper: #ffffff;
    --ink: #5a3a33;
    --accent: #c8175f;
    --band: #5b3d35;
    --backdrop: #e9e4de;
  }
  * { margin: 0; padding: 0; box-sizing: border-box; }
  html, body { width: 1200px; height: 1000px; overflow: hidden; }
  body {
    background: var(--backdrop);
    font-family: "Oswald", "Arial Narrow", sans-serif;
    color: var(--ink);
    position: relative;
  }
  .card {
    position: absolute;
    left: 240px;
    width: 720px;
    height: 410px;
    background: var(--paper);
    box-shadow: 0 6px 18px rgba(60, 40, 30, 0.18);
    overflow: hidden;
  }
  .card--front { top: 70px; }
  .card--back { top: 520px; }
  .edge-accent {
    position: absolute;
    left: 0; right: 0; bottom: 18px;
    height: 7px;
    background: var(--accent);
  }
  .edge-band {
    position: absolute;
    left: 0; right: 0; bottom: 0;
    height: 18px;
    background: var(--band);
  }
  .card-name {
    position: absolute;
    left: 90px;
    top: 150px;
    font-weight: 700;
    font-size: 66px;
    letter-spacing: 0.5px;
    line-height: 1;
    text-transform: uppercase;
  }
  .contact {
    position: absolute;
    left: 0; right: 0;
    top: 50px;
    text-align: center;
    font-weight: 300;
    font-size: 38px;
    line-height: 1.4;
  }
  .services {
    position: absolute;
    left: 0; right: 0;
    top: 218px;
    text-align: center;
    font-weight: 300;
    line-height: 1.3;
  }
  .services-title {
    font-size: 38px;
    text-transform: uppercase;
  }
  .services-title .amp { text-decoration: underline; text-underline-offset: 4px; text-decoration-thickness: 2px; }
  .services-list { font-size: 38px; }
</style>
</head>
<body>
  <section class="card card--front" aria-label="Card front">
    <h1 class="card-name">Maren Dowsett</h1>
    <div class="edge-accent"></div>
    <div class="edge-band"></div>
  </section>

  <section class="card card--back" aria-label="Card back">
    <div class="contact">
      <p class="contact-email">maren@marendowsett.com</p>
      <p class="contact-phone">917.555.0148</p>
    </div>
    <div class="services">
      <p class="services-title">Hospitality <span class="amp">&amp;</span> Home</p>
      <p class="services-list">FF&amp;E, furniture, lighting, textiles, etc.</p>
    </div>
    <div class="edge-accent"></div>
    <div class="edge-band"></div>
  </section>
</body>
</html>
```